Killer business card for bowling event and marketing company

Rolling 'T' Ventures is a sports marketing company that specializes in unique bowling events that provide return on investment for sponsors and memorable experiences for participants and spectators. We need a new business card that simultaneously communicates professionalism and fun. Our preferred colors are black and re

Target Market(s)

Executives in the marketing and sponsorship departments of companies, tourism executives, bowling center owners, and people who love to bowl.

Industry/Entity Type

Business

Contact Information for Business Card

Neil T Farrow
Rolling 'T' Ventures
PO Box 47
Millbrook, Ohio USA 00000
Email: neilt@rollingtventures.example
Mobile: 1-555-318-4762

Requirements
Must have
• Our preferred colors are black and red.
Nice to have
• I am considering the use of the attached image for the back of the card.

```html
<!DOCTYPE html>
<html lang="en">
<head>
<meta charset="utf-8">
<title>Neil T Farrow – Rolling 'T' Ventures</title>
<link rel="stylesheet" href="https://fonts.googleapis.com/css2?family=Jura:wght@500&family=Arimo&display=swap">
<style>
  :root {
    --sand: #cab68a;
    --ink: #2b2a28;
    --charcoal: #3a393a;
    --black: #0a0a0a;
    --red: #b20000;
    --pin-light: #f4f4f4;
    --pin-shade: #b9b9bd;
  }
  html, body {
    margin: 0;
    padding: 0;
    overflow: hidden;
    background: #ffffff;
  }
  .card {
    position: relative;
    width: 1200px;
    height: 667px;
    overflow: hidden;
    background: var(--sand);
    color: var(--ink);
  }
  .card__accent {
    position: absolute;
    left: 0;
    top: 0;
    width: 1200px;
    height: 667px;
  }
  .card__pin {
    position: absolute;
    left: -18px;
    top: 28px;
    width: 122px;
    height: 600px;
    border-radius: 60px 60px 40px 40px / 120px 120px 60px 60px;
    background: linear-gradient(90deg, var(--pin-light) 0%, #e3e3e6 55%, var(--pin-shade) 100%);
  }
  .card__name {
    position: absolute;
    left: 80px;
    top: 38px;
    margin: 0;
    font-family: "Jura", sans-serif;
    font-weight: 500;
    font-size: 106px;
    line-height: 1;
    letter-spacing: -1px;
    white-space: nowrap;
  }
  .card__company {
    position: absolute;
    left: 89px;
    top: 152px;
    margin: 0;
    font-family: "Arimo", sans-serif;
    font-weight: 400;
    font-size: 48px;
    line-height: 1;
    white-space: nowrap;
  }
  .card__icons {
    position: absolute;
    left: 0;
    top: 0;
    width: 1200px;
    height: 667px;
  }
  .contact {
    position: absolute;
    left: 174px;
    margin: 0;
    font-family: "Arimo", sans-serif;
    font-size: 29px;
    line-height: 35px;
    white-space: nowrap;
    font-style: normal;
  }
  .contact--email { top: 257px; }
  .contact--phone { top: 384px; }
  .contact--address { top: 490px; }
</style>
</head>
<body>
<div class="card">
  <svg class="card__accent" viewBox="0 0 1200 667" role="img" aria-label="Sweeping red, black and grey accent band">
    <defs>
      <linearGradient id="accentTone" x1="0" y1="1" x2="1" y2="0">
        <stop offset="0" stop-color="var(--charcoal)"/>
        <stop offset="0.55" stop-color="var(--black)"/>
        <stop offset="0.8" stop-color="var(--red)"/>
        <stop offset="1" stop-color="var(--red)"/>
      </linearGradient>
    </defs>
    <path fill="url(#accentTone)" d="M862,0 L1200,0 L1200,667 L425,667 C650,560 860,330 862,0 Z"/>
  </svg>

  <div class="card__pin" role="img" aria-label="White bowling pin with red neck stripes"></div>

  <h1 class="card__name">Neil T Farrow</h1>
  <p class="card__company">Rolling 'T' Ventures</p>

  <svg class="card__icons" viewBox="0 0 1200 667" aria-hidden="true">
    <g fill="none" stroke="var(--ink)" stroke-width="2.5">
      <line x1="134" y1="300" x2="134" y2="378"/>
      <line x1="134" y1="426" x2="134" y2="502"/>
      <circle cx="134" cy="276" r="24"/>
      <circle cx="134" cy="402" r="24"/>
      <circle cx="134" cy="526" r="24"/>
      <rect x="119" y="265" width="30" height="22"/>
      <polyline points="119,265 134,278 149,265"/>
      <line x1="119" y1="287" x2="130" y2="275"/>
      <line x1="149" y1="287" x2="138" y2="275"/>
    </g>
    <path fill="var(--ink)" d="M126,388 l6,-2 l4,9 l-4,3 c1,5 4,9 8,12 l4,-3 l8,5 l-2,6 c-2,3 -6,3 -10,1 c-9,-5 -15,-13 -17,-22 c-1,-4 0,-7 3,-9 Z"/>
    <path fill="var(--ink)" fill-rule="evenodd" d="M134,508 c-9,0 -15,7 -15,15 c0,10 15,24 15,24 s15,-14 15,-24 c0,-8 -6,-15 -15,-15 Z M134,517 a5,5 0 1 0 0.01,0 Z"/>
  </svg>

  <p class="contact contact--email">neilt@rollingtventures.example</p>
  <p class="contact contact--phone">1-555-318-4762</p>
  <address class="contact contact--address">PO Box 47<br>Millbrook, Ohio USA 00000</address>
</div>
</body>
</html>
```